Membership Drive "End of Spring Sale"

Looking to run a Direct Debit Sale for November 2019 to boost membership number up. This is our slowest area for membership growth, many choose not to do direct debit, special is designed to increase numbers. Artwork will be display via social media (FB and Instagram) as well as in store. Artwork must be eye catching and direct to the customer. Customer should feel a sense of relief with monthly payments instead of one large payment.

Heading: "End of Spring Special"
Direct Debit
$39.95 per month
Terms and conditions apply"
*Offer End 30th November

Slogan:
"More Energy
More Atmosphere
Feel the Difference
Make the change now" can be placed where suits.

below are other promos we had designed on Artwork Hive along with potential photos to be included into this promo

Target Market(s)

Males and Females aged between 18 - 40

Industry/Entity Type

Fitness

Colors

Designer to choose colors to be used in the design.

Requirements
Must have
• Must emphasize "End of Spring Special" $39.95 per month and
• under neath strict terms and conditions apply
• Offer Ends 30th of November
• "All of our contact details"
• Address: 14 Marlow Rd Brindle Park 3187
• Ph: 9581 2706
• www.pulsarfit.com.au
• Design format must come in poster size A0 size, Instagram format, Facebook cover and 800 x 800 for the website
Nice to have
• With the photos attached at least one female and one male in the overall design. Lots of color in relation to Spring and artistic effects to catch peoples eyes.
• Also to include "Celebrating 49 years"

```html
<!DOCTYPE html>
<html lang="en">
<head>
<meta charset="utf-8">
<title>Pulsar Fitness – End of Spring Special</title>
<link href="https://fonts.googleapis.com/css2?family=Anton&family=Permanent+Marker&family=Montserrat:wght@700;800&display=swap" rel="stylesheet">
<style>
  :root{
    --sheet-top:#3a3a3a;
    --sheet-bottom:#242424;
    --label:#e8e8e8;
    --cream:#fbf1c2;
    --peach:#f9cdb4;
    --pink:#f39ab2;
    --ink:#141414;
    --white:#ffffff;
    --red:#d9232e;
    --photo-a:#c79a82;
    --photo-b:#6b4a3e;
  }
  *{box-sizing:border-box;margin:0;padding:0}
  html,body{width:1200px;height:2700px;overflow:hidden}
  body{
    background:linear-gradient(180deg,var(--sheet-top),var(--sheet-bottom));
    font-family:"Montserrat",Arial,sans-serif;
    position:relative;
  }
  .sheet-label{
    position:absolute;left:0;width:1200px;text-align:center;
    color:var(--label);font-weight:800;font-size:26px;letter-spacing:4px;
  }
  .artboard{
    position:absolute;overflow:hidden;
    background:linear-gradient(180deg,var(--cream) 0%,var(--peach) 55%,var(--pink) 100%);
  }
  .artboard > *{position:absolute}
  .brand{
    font-family:"Anton",Impact,sans-serif;color:var(--ink);
    line-height:0.95;letter-spacing:1px;
  }
  .brand small{display:block;font-size:0.42em;letter-spacing:3px}
  .brand .since{display:block;font-family:"Montserrat",Arial,sans-serif;font-weight:700;font-size:0.16em;letter-spacing:2px;margin-top:4px}
  .athletes{
    background:radial-gradient(ellipse at 55% 40%,var(--photo-a) 0%,var(--photo-b) 45%,rgba(107,74,62,0) 72%);
  }
  .band svg{width:100%;height:100%;display:block}
  .band-title{
    font-family:"Permanent Marker",cursive;color:var(--white);
    white-space:nowrap;text-align:center;
  }
  .price{font-family:"Anton",Impact,sans-serif;color:var(--ink);line-height:1}
  .tag{
    display:inline-block;background:var(--red);color:var(--white);
    font-family:"Montserrat",Arial,sans-serif;font-weight:800;letter-spacing:1px;
  }
  .terms{font-weight:800;color:var(--ink);letter-spacing:0.5px}
  .offer{display:flex;align-items:center;font-family:"Anton",Impact,sans-serif;color:var(--ink);line-height:0.95}
  .offer-words{text-align:left}
  .offer-date{text-align:center;line-height:0.9}
  .contact{
    display:flex;justify-content:space-between;
    font-weight:800;color:var(--ink);
  }
</style>
</head>
<body>

<div class="sheet-label" style="top:40px">POSTER</div>
<section class="artboard poster" style="left:188px;top:80px;width:824px;height:1172px">
  <div class="brand" style="left:30px;top:24px;font-size:64px">PULSAR<small>FITNESS</small><span class="since">SINCE 1970</span></div>
  <div class="athletes" role="img" aria-label="Photo of a female boxer punching and a muscular male athlete" style="left:60px;top:10px;width:760px;height:720px"></div>
  <div class="band" style="left:0;top:710px;width:824px;height:160px">
    <svg viewBox="0 0 100 20" preserveAspectRatio="none"><path d="M0 3 L8 2 L15 3.5 L24 1.5 L33 3 L45 2 L56 3.2 L68 1.6 L80 2.8 L90 1.8 L100 3 L100 16 L92 18.5 L84 16.5 L74 19 L63 17 L52 18.8 L40 16.8 L28 19.2 L18 17 L9 19 L0 17 Z" fill="#141414"/></svg>
  </div>
  <div class="band-title" style="left:0;top:748px;width:824px;font-size:62px">END OF SPRING SPECIAL</div>
  <div class="price" style="left:42px;top:900px;font-size:104px">$39.95</div>
  <div class="tag" style="left:44px;top:1016px;font-size:16px;padding:3px 10px">PER MONTH</div>
  <div class="terms" style="left:44px;top:1046px;font-size:17px">TERMS &amp; CONDITIONS APPLY</div>
  <div class="offer" style="left:470px;top:900px;gap:16px">
    <div class="offer-words" style="font-size:70px">OFFER<br>ENDS</div>
    <div class="offer-date"><div style="font-size:140px">30</div><div class="tag" style="font-size:16px;padding:3px 10px">NOVEMBER</div></div>
  </div>
  <div class="contact" style="left:40px;top:1122px;width:744px;font-size:19px">
    <span>14 Marlow Rd Brindle Park</span><span>95812706</span><span>www.pulsarfit.com.au</span>
  </div>
</section>

<div class="sheet-label" style="top:1288px">FACEBOOK COVER</div>
<section class="artboard cover" style="left:80px;top:1344px;width:1040px;height:408px">
  <div class="athletes" role="img" aria-label="Photo of a female boxer punching and a muscular male athlete" style="left:0;top:0;width:470px;height:408px"></div>
  <div class="brand" style="left:16px;top:16px;font-size:40px">PULSAR<small>FITNESS</small></div>
  <div class="band" style="left:360px;top:30px;width:680px;height:112px">
    <svg viewBox="0 0 100 20" preserveAspectRatio="none"><path d="M3 2 L14 4 L26 1.5 L38 3.5 L52 1.8 L66 3.4 L80 1.5 L100 3 L100 16 L88 18.6 L76 16.4 L62 19 L48 16.8 L34 19 L20 17 L8 18.6 L0 16 L4 10 Z" fill="#141414"/></svg>
  </div>
  <div class="band-title" style="left:380px;top:58px;width:660px;font-size:46px">END OF SPRING SPECIAL</div>
  <div class="price" style="left:480px;top:178px;font-size:80px">$39.95</div>
  <div class="tag" style="left:482px;top:270px;font-size:13px;padding:2px 8px">PER MONTH</div>
  <div class="terms" style="left:482px;top:294px;font-size:13px">TERMS &amp; CONDITIONS APPLY</div>
  <div class="offer" style="left:770px;top:178px;gap:12px">
    <div class="offer-words" style="font-size:54px">OFFER<br>ENDS</div>
    <div class="offer-date"><div style="font-size:104px">30</div><div class="tag" style="font-size:12px;padding:2px 8px">NOVEMBER</div></div>
  </div>
  <div class="contact" style="left:480px;top:362px;width:530px;font-size:15px">
    <span>14 Marlow Rd Brindle Park</span><span>95812706</span><span>www.pulsarfit.com.au</span>
  </div>
</section>

<div class="sheet-label" style="top:1800px">INSTAGRAM</div>
<section class="artboard square" style="left:204px;top:1852px;width:792px;height:788px">
  <div class="brand" style="left:26px;top:22px;font-size:56px">PULSAR<small>FITNESS</small><span class="since">SINCE 1970</span></div>
  <div class="athletes" role="img" aria-label="Photo of a female boxer punching and a muscular male athlete" style="left:60px;top:10px;width:730px;height:470px"></div>
  <div class="band" style="left:0;top:470px;width:792px;height:124px">
    <svg viewBox="0 0 100 20" preserveAspectRatio="none"><path d="M0 3 L10 1.8 L22 3.4 L34 1.6 L48 3.2 L60 1.8 L74 3.4 L86 1.6 L100 3 L100 16.5 L88 18.8 L76 16.6 L62 19 L48 16.8 L34 19 L20 16.8 L8 18.8 L0 16.5 Z" fill="#141414"/></svg>
  </div>
  <div class="band-title" style="left:0;top:500px;width:792px;font-size:54px">END OF SPRING SPECIAL</div>
  <div class="price" style="left:40px;top:612px;font-size:84px">$39.95</div>
  <div class="tag" style="left:42px;top:706px;font-size:13px;padding:2px 8px">PER MONTH</div>
  <div class="terms" style="left:42px;top:730px;font-size:14px">TERMS &amp; CONDITIONS APPLY</div>
  <div class="offer" style="left:470px;top:612px;gap:12px">
    <div class="offer-words" style="font-size:56px">OFFER<br>ENDS</div>
    <div class="offer-date"><div style="font-size:106px">30</div><div class="tag" style="font-size:12px;padding:2px 8px">NOVEMBER</div></div>
  </div>
  <div class="contact" style="left:40px;top:760px;width:712px;font-size:15px">
    <span>14 Marlow Rd Brindle Park</span><span>95812706</span><span>www.pulsarfit.com.au</span>
  </div>
</section>

</body>
</html>
```